New Business and Accounting Software need a Web Site

The website is for a Business and Accounting Software that has 8 products.
Each product has its owns logo and color, when you do the design have in consideration that we are looking the experience that when you change from one product page to another the look and feel adjust to the color and logo of the product.
The product are:
Ventas (Sales)
Compras (Purchases)
Contabilidad (Accounting)
Presupuesto (Budget)
Inventarios (Inventory)
Bancos (Banks)
NĂ³mina RH (Human Resources Payroll)
CRM (Customer Relationship Manager)

You can see how the main logo and variations are used in each page
- https://www.ufta.com/
- https://www.vemi.com/
- https://www.prulvin.com/

Our goal is to be similar to them.

I have created a word document to explain what I want.
You need to design:
1 Home Page
1 Product Landing Page
1 Product Detail Page
1 Price Page

I am attaching:
1. Main Logo
2. 8 Product Logos
3. Website Idea, you can create your own idea.

You are welcome to use other icons for the each product if you want.

Target Market(s)

Independet professionals and Small and Medium Companies

Industry/Entity Type

Business and Accounting Software

Coding

Coded - Design and coding required

Colors
0054AA
0677BA
7BADD7
CADEEF
E8F1F8

Requirements
Must have
• Must show all products in the main page

```html
<!DOCTYPE html>
<html lang="es">
<head>
<meta charset="utf-8">
<title>Cuentix — Sistema Contable y Facturación en la nube</title>
<link href="https://fonts.googleapis.com/css2?family=Poppins:wght@300;400;500;600&display=swap" rel="stylesheet">
<style>
:root{
  --blue:#0054AA;
  --blue-2:#0677BA;
  --blue-3:#7BADD7;
  --blue-4:#CADEEF;
  --blue-5:#E8F1F8;
  --hero:#D4E5F6;
  --grey-bg:#F7F7F7;
  --text:#6b6b6b;
  --green:#5DBF1E;
  --line:#e4e4e4;
}
*{margin:0;padding:0;box-sizing:border-box}
html,body{width:1200px;height:3747px;overflow:hidden}
body{font-family:'Poppins',sans-serif;color:var(--text);background:#fff;position:relative}
a{color:inherit;text-decoration:none}
.abs{position:absolute}
.pill{border-radius:30px;display:flex;align-items:center;justify-content:center;font-size:14px}
.btn-blue{background:var(--blue);color:#fff}
.brand{display:flex;align-items:center;gap:10px;color:var(--blue);font-weight:600}
.brand .dot{border-radius:50%;background:var(--blue);flex:none}

/* header */
.site-header{position:absolute;top:0;left:0;width:1200px;height:75px;background:#fff;z-index:3}
.site-header .brand{position:absolute;left:60px;top:8px;font-size:38px}
.site-header .brand .dot{width:54px;height:54px}
.main-nav{position:absolute;top:26px;left:548px;display:flex;gap:0;font-size:14px;color:#555}
.main-nav a{position:absolute;white-space:nowrap}
.nav-btn{position:absolute;top:20px;height:38px}

/* hero */
.hero{position:absolute;top:75px;left:0;width:1200px;height:620px}
.hero h1{position:absolute;top:42px;width:1200px;text-align:center;color:var(--blue);font-weight:600;font-size:39px;line-height:49px}
.hero p{position:absolute;top:146px;width:1200px;text-align:center;font-size:14px;color:#555}
.shot{position:absolute;border-radius:2px}

/* products */
.section-title{position:absolute;width:1200px;text-align:center;color:var(--blue);font-weight:500;font-size:26px}
.product-grid{position:absolute;left:60px;top:815px;width:1080px;height:218px;display:grid;grid-template-columns:repeat(4,1fr);grid-template-rows:103px 115px}
.product-tile{display:flex;align-items:center;justify-content:center;border-right:1px solid var(--line)}
.product-tile:nth-child(4n){border-right:none}
.product-tile:nth-child(-n+4){border-bottom:1px solid var(--line)}
.product-logo{display:flex;align-items:center;gap:8px}
.product-logo .dot{width:48px;height:48px;border-radius:50%}
.product-logo .name{color:var(--blue);font-weight:600;font-size:32px;line-height:32px}
.product-logo .sub{font-size:10px;letter-spacing:4px;text-transform:uppercase;font-weight:400;margin-top:1px}

/* audience cards */
.audience{position:absolute;top:1090px;left:0;width:1200px;height:772px;background:var(--grey-bg)}
.card{position:absolute;display:flex;overflow:hidden;border-radius:4px}
.card-body{padding:24px 20px;display:flex;flex-direction:column}
.card h3{font-size:16px;font-weight:500;margin-bottom:10px}
.card p{font-size:13.5px;line-height:22.5px;font-weight:300}
.card .more{margin-top:auto;font-size:13.5px;font-weight:600}
.card.white{background:#fff}
.card.white h3,.card.white .more{color:var(--blue)}
.card.color{color:#fff}
.photo{flex:none}

/* tabs */
.tabs{position:absolute;top:2003px;left:0;width:1200px;display:flex;justify-content:center;gap:14px}
.tab{height:37px;padding:0 19px;border:1px solid #9ab;border-radius:20px;display:flex;align-items:center;font-size:13.5px;color:#444}
.tab.active{background:var(--blue);color:#fff;border-color:var(--blue)}
.feature h2{position:absolute;left:61px;top:2110px;font-size:16.5px;font-weight:600;color:var(--blue)}
.feature p{position:absolute;left:61px;top:2145px;width:495px;font-size:13.8px;line-height:22.5px;color:#777}
.ticks{position:absolute;left:61px;top:2262px;list-style:none;font-size:13.8px;color:#777}
.ticks li{display:flex;align-items:center;gap:10px;height:25.5px}

/* solutions */
.solution{position:absolute;width:205px;height:205px;border-radius:50%;background:var(--blue);color:#fff;text-align:center;display:flex;flex-direction:column;align-items:center;justify-content:center;padding:0 24px}
.solution h3{font-size:16.5px;font-weight:500;margin-bottom:10px;line-height:22px}
.solution p{font-size:13.5px;line-height:22.5px;font-weight:300}
.badge{position:absolute;width:44px;height:44px;border-radius:50%;background:var(--blue-3);color:#fff;font-size:16px;display:flex;align-items:center;justify-content:center;border:2px solid #fff}

/* cta */
.cta-title{position:absolute;left:61px;top:3050px;color:#fff;font-size:27px;font-weight:500;line-height:38px}

/* footer */
.newsletter{position:absolute;top:3358px;left:427px;width:505px;height:37px;background:var(--blue-3);color:#fff;border-radius:20px;font-size:13.5px;padding-left:20px;display:flex;align-items:center}
.footer-col{position:absolute;top:3476px;font-size:13px;color:#666}
.footer-col h4{color:var(--blue);font-weight:600;font-size:13.5px;margin-bottom:12px}
.footer-col li{list-style:none;height:26.5px}
.contact li{display:flex;gap:10px;align-items:center;height:36px}
.social{display:flex;gap:14px}
.social span{width:36px;height:36px;border-radius:50%;background:var(--blue)}
.copyright{position:absolute;top:3713px;width:1200px;text-align:center;font-size:12px;color:var(--blue)}
</style>
</head>
<body>

<header class="site-header">
  <a class="brand" href="#"><span class="dot"></span>cuentix</a>
  <nav class="main-nav">
    <a style="left:0;color:var(--blue);display:flex;gap:6px;align-items:center" href="#"><svg width="13" height="13"><circle cx="6.5" cy="6.5" r="5.5" fill="none" stroke="#0054AA" stroke-width="2"/></svg>Inicio</a>
    <a style="left:95px" href="#">Soluciones</a>
    <a style="left:206px" href="#">Planes</a>
    <a style="left:282px" href="#">Contacto</a>
  </nav>
  <a class="nav-btn pill btn-blue" style="left:927px;width:87px" href="#">Sign In</a>
  <a class="nav-btn pill btn-blue" style="left:1038px;width:102px" href="#">Free Trial</a>
</header>

<section class="hero">
  <svg class="abs" style="left:0;top:0" width="1200" height="620" viewBox="0 0 1200 620">
    <path d="M0 0H1200V470C1120 520 1060 480 975 470L975 620H225L225 500C140 470 60 480 0 510Z" fill="#D4E5F6"/>
  </svg>
  <h1>Sistema Contable y<br>Facturación en la nube</h1>
  <p>Plataforma 100% en línea para facturar de manera rápida, ágil y sencilla</p>
  <a class="abs pill btn-blue" style="left:549px;top:187px;width:102px;height:36px" href="#">Free Trial</a>
  <div class="shot" role="img" aria-label="Captura del panel de trabajo con lista de tareas" style="left:225px;top:240px;width:750px;height:362px;background:linear-gradient(#0054AA 0 20px,#f4f6f9 20px 335px,#0054AA 335px)"></div>
</section>

<h2 class="section-title" style="top:757px">Por Producto</h2>
<div class="product-grid">
  <div class="product-tile"><div class="product-logo"><span class="dot" style="background:#E8862A"></span><div><div class="name">cuentix</div><div class="sub" style="color:#E8862A">ventas</div></div></div></div>
  <div class="product-tile"><div class="product-logo"><span class="dot" style="background:#2AA7B8"></span><div><div class="name">cuentix</div><div class="sub" style="color:#2AA7B8">compras</div></div></div></div>
  <div class="product-tile"><div class="product-logo"><span class="dot" style="background:#C2357A"></span><div><div class="name">cuentix</div><div class="sub" style="color:#C2357A;letter-spacing:2px">contabilidad</div></div></div></div>
  <div class="product-tile"><div class="product-logo"><span class="dot" style="background:#B0315E"></span><div><div class="name">cuentix</div><div class="sub" style="color:#B0315E;letter-spacing:2px">inventarios</div></div></div></div>
  <div class="product-tile"><div class="product-logo"><span class="dot" style="background:#555"></span><div><div class="name">cuentix</div><div class="sub" style="color:#555">bancos</div></div></div></div>
  <div class="product-tile"><div class="product-logo"><span class="dot" style="background:#17A7A0"></span><div><div class="name">cuentix</div><div class="sub" style="color:#17A7A0;letter-spacing:2px">presupuesto</div></div></div></div>
  <div class="product-tile"><div class="product-logo"><span class="dot" style="background:#47B45A"></span><div><div class="name">cuentix</div><div class="sub" style="color:#47B45A;letter-spacing:3px">nómina rh</div></div></div></div>
  <div class="product-tile"><div class="product-logo"><span class="dot" style="background:#6A4FC2"></span><div><div class="name">cuentix</div><div class="sub" style="color:#6A4FC2">crm</div></div></div></div>
</div>

<section class="audience">
  <svg class="abs" style="left:0;top:-2px" width="1200" height="180" viewBox="0 0 1200 180">
    <path d="M0 0H1200V80C1080 160 960 170 820 120C700 80 620 30 480 50C320 70 230 120 120 80C60 60 30 30 0 20Z" fill="#fff"/>
  </svg>
</section>
<h2 class="section-title" style="top:1267px">¿Qué es CUENTIX?</h2>

<article class="card white" style="left:60px;top:1330px;width:525px;height:225px">
  <div class="card-body" style="width:266px"><h3>Prosesional</h3><p>Lorem Ipsum is simply dummy text of the printing and typesetting industry. Lorem Ipsum has been the industry's standard dummy text.</p><a class="more" href="#">más información</a></div>
  <div class="photo" role="img" aria-label="Fotografía de profesional independiente trabajando con laptop" style="width:259px;background:linear-gradient(135deg,#b9a79a,#e6e2dd 60%,#cfc9c2)"></div>
</article>
<article class="card white" style="left:616px;top:1330px;width:524px;height:225px">
  <div class="card-body" style="width:266px"><h3>Contador</h3><p>Lorem Ipsum is simply dummy text of the printing and typesetting industry. Lorem Ipsum has been the industry's standard dummy text.</p><a class="more" href="#">más información</a></div>
  <div class="photo" role="img" aria-label="Fotografía de calculadora y documentos contables" style="width:258px;background:linear-gradient(135deg,#6f6a64,#c9c5bf 55%,#e9e7e3)"></div>
</article>
<article class="card color" style="left:60px;top:1583px;width:250px;height:225px;background:var(--blue-3)">
  <div class="card-body"><h3>Micro</h3><p>Lorem Ipsum is simply dummy text of the printing and typesetting industry. Lorem Ipsum has been the industry's standard dummy text.</p><a class="more" href="#">más información</a></div>
</article>
<article class="card color" style="left:334px;top:1583px;width:251px;height:225px;background:var(--green)">
  <div class="card-body"><h3>PYME</h3><p>Lorem Ipsum is simply dummy text of the printing and typesetting industry. Lorem Ipsum has been the industry's standard dummy text.</p><a class="more" href="#">más información</a></div>
</article>
<article class="card color" style="left:616px;top:1583px;width:524px;height:225px;background:var(--blue)">
  <div class="card-body" style="width:266px"><h3>Empresarial</h3><p>Lorem Ipsum is simply dummy text of the printing and typesetting industry. Lorem Ipsum has been the industry's standard dummy text.</p><a class="more" href="#">más información</a></div>
  <div class="photo" role="img" aria-label="Fotografía de ejecutivos estrechando manos" style="width:258px;background:linear-gradient(135deg,#f1f2f4,#8d96a3 60%,#3b4250)"></div>
</article>

<h2 class="section-title" style="top:1939px">¿Qué es CUENTIX?</h2>
<nav class="tabs">
  <a class="tab active" href="#">Ventas</a>
  <a class="tab" href="#">Compras</a>
  <a class="tab" href="#">Contabilidad</a>
  <a class="tab" href="#">Inventarios</a>
  <a class="tab" href="#">Bancos</a>
  <a class="tab" href="#">Presupuesto</a>
  <a class="tab" href="#">Nomina RH</a>
  <a class="tab" href="#">CRM</a>
</nav>

<section class="feature">
  <h2>Lorem Ipsum is simply dummy text.</h2>
  <p>Lorem Ipsum is simply dummy text of the printing and typesetting industry. Lorem Ipsum has been the industry's standard dummy text ever since the 1500s, when an unknown printer took a galley of type and scrambled it to make a type specimen book. It has survived not only five centuries, but also the leap into electronic typesetting.</p>
  <ul class="ticks">
    <li><svg width="16" height="16"><circle cx="8" cy="8" r="7" fill="none" stroke="#0054AA" stroke-width="2"/><path d="M4.5 8l2.5 2.5 4.5-5" fill="none" stroke="#0054AA" stroke-width="1.8"/></svg>Lorem Ipsum is simply dummy text of the printing and typesetting.</li>
    <li><svg width="16" height="16"><circle cx="8" cy="8" r="7" fill="none" stroke="#0054AA" stroke-width="2"/><path d="M4.5 8l2.5 2.5 4.5-5" fill="none" stroke="#0054AA" stroke-width="1.8"/></svg>Lorem Ipsum is simply dummy text of the printing and typesetting.</li>
    <li><svg width="16" height="16"><circle cx="8" cy="8" r="7" fill="none" stroke="#0054AA" stroke-width="2"/><path d="M4.5 8l2.5 2.5 4.5-5" fill="none" stroke="#0054AA" stroke-width="1.8"/></svg>Lorem Ipsum is simply dummy text of the printing and typesetting.</li>
  </ul>
  <a class="abs pill btn-blue" style="left:60px;top:2375px;width:112px;height:36px" href="#">Read More</a>
  <span class="abs" style="left:895px;top:2068px;width:246px;height:246px;border-radius:50%;background:#DCE9F5"></span>
  <span class="abs" style="left:641px;top:2272px;width:110px;height:110px;border-radius:50%;background:var(--blue)"></span>
  <div class="shot" role="img" aria-label="Captura del módulo de ventas con vista de factura" style="left:664px;top:2134px;width:451px;height:215px;background:linear-gradient(#0054AA 0 10px,#f5f7fa 10px 207px,#0054AA 207px)"></div>
</section>

<h2 class="section-title" style="top:2490px">Nuestras Soluciones</h2>
<div class="solution" style="left:60px;top:2600px"><h3>Paga por Uso</h3><p>Paga solo por las funcionalidades que te interesan.</p></div>
<span class="badge" style="left:190px;top:2563px">1</span>
<div class="solution" style="left:319px;top:2600px"><h3>Sin Contrato</h3><p>Una vez que lo pruebes no te querrás ir. No necesitamos contrato</p></div>
<span class="badge" style="left:456px;top:2563px">2</span>
<div class="solution" style="left:588px;top:2600px"><h3>En la Nube</h3><p>Desde cualquier lugar y a cualquier hora siempre disponible</p></div>
<span class="badge" style="left:719px;top:2555px">3</span>
<div class="solution" style="left:850px;top:2575px;width:205px;height:205px"><h3>Múltiples Dispositivos</h3><p>Accesa a tu información desde tu conmputadora personal, tu tableta o teléfono inteligente</p></div>
<span class="badge" style="left:970px;top:2552px">4</span>

<section class="cta">
  <svg class="abs" style="left:0;top:2880px" width="1200" height="402" viewBox="0 0 1200 402">
    <path d="M0 30C120 -10 250 20 380 70C520 120 650 140 780 110C900 80 1000 70 1100 130C1150 160 1180 180 1200 190V402H0Z" fill="#6D9FD4"/>
  </svg>
  <div class="abs" role="img" aria-label="Fotografía de hombre sonriente trabajando en laptop" style="left:722px;top:2852px;width:376px;height:376px;border-radius:50%;background:radial-gradient(circle at 45% 40%,#c7d6e6,#6f8fb5 70%,#3e5f8e)"></div>
  <h2 class="cta-title">¿Qué esperas para crear una cuenta<br>gratis en CUENTIX?</h2>
  <a class="abs pill" style="left:60px;top:3170px;width:178px;height:35px;background:#fff;color:#555" href="#">Crear Cuenta Gratis</a>
</section>

<footer>
  <a class="brand abs" style="left:60px;top:3338px;font-size:38px" href="#"><span class="dot" style="width:54px;height:54px"></span>cuentix</a>
  <div class="newsletter">Reciba las actualizaciones de Cuentix</div>
  <a class="abs pill btn-blue" style="left:951px;top:3358px;width:122px;height:37px" href="#">Suscribirme</a>
  <span class="abs" style="left:0;top:3441px;width:1200px;height:1px;background:var(--line)"></span>
  <div class="footer-col" style="left:61px"><h4>Quick Links</h4><ul><li>Inicio</li><li>Soluciones</li><li>Planes</li><li>Contacto</li></ul></div>
  <div class="footer-col" style="left:338px"><h4>Products</h4><ul><li>Ventas</li><li>Compras</li><li>Contabilidad</li><li>Inventarious</li><li>Bancos</li><li>Presupuesto</li><li>Nomina RH</li></ul></div>
  <div class="footer-col contact" style="left:613px"><h4>Contact Us</h4><ul>
    <li><svg width="16" height="18"><path d="M8 17C8 17 2 10 2 6.5a6 6 0 0 1 12 0C14 10 8 17 8 17z" fill="none" stroke="#7BADD7" stroke-width="1.4"/><circle cx="8" cy="6.5" r="2.2" fill="none" stroke="#7BADD7" stroke-width="1.4"/></svg>Barrio Norte, Heredia</li>
    <li><svg width="16" height="16"><path d="M3 1.5l3 .5 1 3.5-2 1.5a9 9 0 0 0 4.5 4.5l1.5-2 3.5 1 .5 3c-6 1-13-6-12-12z" fill="none" stroke="#7BADD7" stroke-width="1.3"/></svg>4000-7315</li>
    <li><svg width="16" height="12"><rect x="1" y="1" width="14" height="10" fill="none" stroke="#7BADD7" stroke-width="1.3"/><path d="M1 1l7 6 7-6" fill="none" stroke="#7BADD7" stroke-width="1.3"/></svg>hola@cuentix.co</li>
  </ul></div>
  <div class="footer-col" style="left:890px"><h4>Social Links</h4><div class="social"><span role="img" aria-label="Red profesional"></span><span role="img" aria-label="Red social"></span></div></div>
  <p class="copyright">© 2022 Cuentix. Todos los derechos reservados.</p>
</footer>

</body>
</html>
```